Wine Label for a wine from Tuscany, Italy

We need a wine label for a white and red wine, can be the same label or can be somewhat differentiated with any variation you feel would be good.. These two wines come from Tuscany, Italy. Wine labels from Tuscany Italy tend to be traditional. We are open to traditional looking labels but also more modern, eye catching too. We want to convey a sense of elegance, importance, great wine. I am attaching some examples of labels we like from Tuscany, also a label that was designed for us recently by one of you, which we LOVE. No wine glasses, wine bottles or grapes featured on the label please. We tend to like the white background. No blue please.

Target Market(s)

More women than men purchase wine, but it needs to appeal to both sexes.

Requirements
Must have
• Wine Name: Casa Morel or Casa morel
• Type/Varletal: Rosso Toscano (White is Vermentino)
• Vintage (year): 2018
• That is all the text we want on the label, thanks
Nice to have
• Clean, something that makes someone want to grab this wine bottle off the shelf!
Should not have
• Images of Wine glass, wine bottles, grapes
• Do not use the color blue please.

```html
<!DOCTYPE html>
<html lang="it">
<head>
<meta charset="utf-8">
<title>Casa morel – Vermentino Toscano 2018</title>
<link rel="stylesheet" href="https://fonts.googleapis.com/css2?family=Pinyon+Script&family=Arimo:wght@400;700&display=swap">
<style>
  :root {
    --backdrop: #ececea;
    --paper: #f8f7f4;
    --ink: #1c1c1c;
    --gold: #b08f3a;
    --portrait-light: #8a8a8a;
    --portrait-dark: #1e1e1e;
  }
  * { margin: 0; padding: 0; box-sizing: border-box; }
  html, body {
    width: 1200px;
    height: 1200px;
    overflow: hidden;
    background: var(--backdrop);
  }
  .canvas {
    width: 1200px;
    height: 1200px;
    display: flex;
    align-items: center;
    justify-content: center;
  }
  .label {
    position: relative;
    width: 800px;
    height: 1150px;
    background: var(--paper);
    box-shadow: 0 2px 10px rgba(0,0,0,0.12);
    overflow: hidden;
  }
  .label__portrait {
    position: absolute;
    top: 58px;
    left: 50%;
    transform: translateX(-50%);
    width: 630px;
    height: 630px;
    border-radius: 50%;
    background: radial-gradient(circle at 45% 45%, var(--portrait-light) 0%, #5a5a5a 45%, var(--portrait-dark) 100%);
  }
  .label__name {
    position: absolute;
    top: 715px;
    left: 40px;
    right: 40px;
    text-align: center;
    font-family: "Pinyon Script", cursive;
    font-weight: 400;
    font-size: 124px;
    line-height: 1.2;
    letter-spacing: 8px;
    white-space: nowrap;
    color: var(--ink);
  }
  .label__varietal {
    position: absolute;
    top: 960px;
    left: 0;
    width: 100%;
    text-align: center;
    font-family: "Arimo", sans-serif;
    font-weight: 400;
    font-size: 54px;
    line-height: 1.2;
    letter-spacing: 4px;
    white-space: nowrap;
    color: var(--gold);
  }
  .label__vintage {
    position: absolute;
    top: 1036px;
    left: 0;
    width: 100%;
    text-align: center;
    font-family: "Arimo", sans-serif;
    font-weight: 700;
    font-size: 54px;
    line-height: 1.2;
    letter-spacing: 3px;
    color: var(--ink);
  }
</style>
</head>
<body>
  <main class="canvas">
    <article class="label">
      <div class="label__portrait" role="img" aria-label="Engraved classical marble bust in a circular medallion"></div>
      <h1 class="label__name">Casa morel</h1>
      <p class="label__varietal">VERMENTINO TOSCANO</p>
      <p class="label__vintage">2018</p>
    </article>
  </main>
</body>
</html>
```